Skylorn Holiday Greetings Card

We are looking for a digital / Print Holliday Greetings card to email out to our customers. We really want something different but must remain within the aviation industry. OUr customers are primarily Airlines and the message needs to be generic and non-religious.
It is a joyful time and we want to thank them for their continuous support and wish them the best over the holidays and a happy New Year, Text will be provided in word format as an upload file.

See our Website for overall brand . Althogh we we have uploaded some past samples it is only as a reference. We need somehting new.

www.skylornworks.example

Target Market(s)

airlines our customers

Industry/Entity Type

Aviation

Colors
0555a3
3276b5
85abd2
ec1f27

Requirements
Must have
• Our logo
• Our colors
• aviation and technical feel
• bilingual message (supplied by us in the uploaded files)
• Something unique
• our website
Nice to have
• Animation on the digital side
• Although the colors listed below are our brand colors we are open to suggestions.
Should not have
• Religious messages or images
• Santa Clause
• Reindeers

```html
<!DOCTYPE html>
<html lang="en">
<head>
<meta charset="utf-8">
<title>Skylorn Holiday Greetings Card</title>
<link rel="stylesheet" href="https://fonts.googleapis.com/css2?family=Oswald:wght@400;500&display=swap">
<style>
  :root {
    --backdrop: #a0e8ea;
    --brand-deep: #0555a3;
    --brand-mid: #3276b5;
    --brand-light: #85abd2;
    --brand-red: #ec1f27;
    --sky-top: #2a5aa3;
    --sky-bottom: #3a73b8;
    --contrail: #e6eff7;
    --greeting: #dceaf3;
    --white: #ffffff;
  }
  html, body {
    margin: 0;
    padding: 0;
    width: 1200px;
    height: 1200px;
    overflow: hidden;
    background: var(--backdrop);
  }
  .canvas {
    position: relative;
    width: 1200px;
    height: 1200px;
    display: flex;
    align-items: center;
    justify-content: center;
  }
  .card {
    position: relative;
    width: 1100px;
    height: 680px;
    background: var(--brand-deep);
    overflow: hidden;
  }
  .card-art {
    position: absolute;
    inset: 0;
    width: 100%;
    height: 100%;
  }
  .brand {
    position: absolute;
    left: 36px;
    top: 28px;
    display: flex;
    align-items: center;
    gap: 12px;
    color: var(--white);
    font-family: "Oswald", sans-serif;
  }
  .brand-mark {
    width: 22px;
    height: 22px;
    background: var(--white);
  }
  .brand-name {
    font-size: 26px;
    font-weight: 500;
    line-height: 1;
  }
  .brand-details {
    font-size: 10px;
    font-weight: 400;
    line-height: 1.35;
    letter-spacing: 0.04em;
  }
  .greeting {
    position: absolute;
    left: 560px;
    top: 370px;
    margin: 0;
    font-family: "Oswald", sans-serif;
    font-weight: 400;
    font-size: 80px;
    line-height: 1;
    color: var(--greeting);
    letter-spacing: -0.005em;
  }
  .greeting span { display: block; white-space: nowrap; }
  .greeting .line-en { margin-left: -34px; }
  .horizon-mark {
    position: absolute;
    left: 330px;
    top: 636px;
    width: 130px;
    height: 20px;
  }
</style>
</head>
<body>
  <main class="canvas">
    <article class="card">
      <svg class="card-art" viewBox="0 0 1100 680" preserveAspectRatio="none">
        <defs>
          <linearGradient id="sky-gradient" x1="0" y1="0" x2="0" y2="1">
            <stop offset="0" stop-color="var(--sky-top)"/>
            <stop offset="1" stop-color="var(--sky-bottom)"/>
          </linearGradient>
          <linearGradient id="contrail-gradient" x1="0" y1="0" x2="0" y2="1">
            <stop offset="0" stop-color="var(--contrail)" stop-opacity="0.95"/>
            <stop offset="0.6" stop-color="var(--contrail)" stop-opacity="0.75"/>
            <stop offset="1" stop-color="var(--contrail)" stop-opacity="0.55"/>
          </linearGradient>
        </defs>
        <polygon class="band band-mid" points="231,0 308,0 132,680 55,680" fill="var(--brand-mid)"/>
        <polygon class="band band-light" points="308,0 407,0 209,680 132,680" fill="var(--brand-light)"/>
        <polygon class="sky" points="407,0 1100,0 1100,680 209,680" fill="url(#sky-gradient)"/>
        <polygon class="contrail-photo" role="img" aria-label="Photo of a jet airliner climbing through clear blue sky, trailing long white contrails" points="588,196 604,196 408,690 368,690" fill="url(#contrail-gradient)"/>
      </svg>

      <div class="brand">
        <div class="brand-mark"></div>
        <div class="brand-name">Skylorn</div>
        <div class="brand-details">Aircraft Support Services<br>www.skylornworks.example</div>
      </div>

      <h1 class="greeting">
        <span class="line-fr">Joyeuses Fetes</span>
        <span class="line-en">Happy Holiday</span>
      </h1>

      <svg class="horizon-mark" viewBox="0 0 130 20">
        <line x1="0" y1="12" x2="130" y2="12" stroke="var(--brand-light)" stroke-width="1" opacity="0.7"/>
        <circle cx="62" cy="3" r="2" fill="var(--brand-red)"/>
        <circle cx="62" cy="12" r="2" fill="var(--brand-red)"/>
      </svg>
    </article>
  </main>
</body>
</html>
```